Need help revamping our cards for Prescription Assistance Program

Would like to go with something in a Black Theme that grabs attention and looks official. I have included some of our previous designs. The Blue/White version is our most current version so would like to follow its format regarding the information. Perhaps, one side white, the other black(might be different/catchy)
Cards are not to have pharmacy logos. Would like to have the ability to update cards with new member IDs. Would also desire a continued relationship with the designer to update and/or modify for regional needs.
Thank you

needs information stacked on the right side for easy viewing whilst flipping through a stack of competitor's cards

please include VELMAR Code

Target Market(s)

pharmacies(pharmacist, techs), general public

Requirements
Must have
• eye catching, official looking, information aragned in an easy to view format, desired to standout if in an stack of 20 other cards
Should not have
• pharmacy logos

```html
<!DOCTYPE html>
<html lang="en">
<head>
<meta charset="UTF-8">
<title>MedLift Discount Prescription Card</title>
<link href="https://fonts.googleapis.com/css2?family=Lato:wght@400;700;900&display=swap" rel="stylesheet">
<style>
  :root {
    --crimson: #c8103a;
    --ink: #1a1a1a;
    --card-black: #161616;
    --paper: #ffffff;
    --backdrop: #e9e6e6;
  }
  * { margin: 0; padding: 0; box-sizing: border-box; }
  html, body { width: 1200px; height: 800px; overflow: hidden; }
  body {
    background: var(--backdrop);
    font-family: "Lato", Arial, sans-serif;
    position: relative;
  }
  .card {
    position: absolute;
    left: 300px;
    width: 600px;
    height: 343px;
    overflow: hidden;
    box-shadow: 0 6px 18px rgba(0,0,0,0.18);
  }
  .card--front { top: 30px; background: var(--paper); }
  .card--back { top: 427px; background: var(--card-black); }

  .pill-band {
    position: absolute;
    left: 0;
    background: var(--crimson);
    border-radius: 0 48px 48px 0;
    color: var(--paper);
  }
  .card--front .pill-band { top: 38px; width: 318px; height: 96px; padding: 16px 20px 0 26px; }
  .notice-title { font-size: 25px; font-weight: 400; text-decoration: underline; text-underline-offset: 3px; line-height: 1.1; }
  .notice-text { font-size: 12px; line-height: 1.3; margin-top: 6px; }

  .rule {
    position: absolute;
    height: 4px;
    background: var(--crimson);
  }
  .card--front .rule { top: 130px; left: 318px; width: 250px; }
  .card--back .rule { top: 178px; left: 290px; width: 310px; }

  .brand {
    position: absolute;
    display: flex;
    align-items: center;
    gap: 10px;
  }
  .brand-dot {
    width: 34px; height: 34px;
    border-radius: 50%;
    border: 6px solid var(--crimson);
    flex: none;
  }
  .brand-text { display: flex; flex-direction: column; }
  .brand-name { font-size: 38px; font-weight: 900; line-height: 1; letter-spacing: -1px; }
  .brand-tagline { font-size: 7px; letter-spacing: 1.4px; font-weight: 700; margin-top: 3px; }
  .card--front .brand { top: 56px; right: 30px; }
  .card--front .brand-name, .card--front .brand-tagline { color: var(--ink); }
  .card--back .brand { top: 116px; left: 28px; }
  .card--back .brand-dot { border-color: var(--paper); }
  .card--back .brand-name, .card--back .brand-tagline { color: var(--paper); }
  .card--back .pill-band { top: 100px; width: 300px; height: 92px; }

  .feature-list { position: absolute; list-style: none; }
  .feature-list li {
    display: flex; align-items: center; gap: 14px;
    font-size: 15px; font-weight: 700; color: var(--ink);
    line-height: 1.15; margin-bottom: 12px;
  }
  .ring {
    width: 22px; height: 22px;
    border-radius: 50%;
    border: 5px solid var(--crimson);
    flex: none;
  }
  .feature-list--left { top: 152px; left: 32px; }
  .feature-list--right { top: 218px; left: 340px; width: 240px; }

  .member-info { position: absolute; top: 206px; left: 26px; list-style: none; }
  .member-info li {
    display: flex; align-items: center; gap: 14px;
    color: var(--paper); font-size: 16px; letter-spacing: 1px; margin-bottom: 12px;
  }
  .member-icon {
    width: 24px; height: 24px; border-radius: 50%;
    background: var(--crimson); flex: none;
  }

  .code-box {
    position: absolute;
    top: 132px; left: 440px;
    width: 96px; height: 96px;
    background: var(--paper);
    border: 4px solid var(--crimson);
    display: flex; flex-direction: column; align-items: center; justify-content: center;
    color: var(--crimson);
  }
  .code-label { font-size: 15px; letter-spacing: 1.5px; }
  .code-number { font-size: 26px; letter-spacing: 1px; line-height: 1.1; }
</style>
</head>
<body>
  <section class="card card--front" aria-label="Card front">
    <div class="pill-band">
      <p class="notice-title">Attention pharmacist</p>
      <p class="notice-text">If you are unable to process a prescription<br>through the programme, call (800) 555-0142</p>
    </div>
    <div class="rule"></div>
    <div class="brand">
      <span class="brand-dot"></span>
      <div class="brand-text">
        <span class="brand-name">MedLift</span>
        <span class="brand-tagline">DISCOUNT PRESCRIPTION DRUG CARD</span>
      </div>
    </div>
    <ul class="feature-list feature-list--left">
      <li><span class="ring"></span>100% HIPAA Compliant</li>
      <li><span class="ring"></span>upto 90% instant savings</li>
    </ul>
    <ul class="feature-list feature-list--right">
      <li><span class="ring"></span>Largest savings on FAST MOVERS</li>
      <li><span class="ring"></span>Always savings to LOWER of PRICING</li>
    </ul>
  </section>

  <section class="card card--back" aria-label="Card back">
    <div class="pill-band"></div>
    <div class="brand">
      <span class="brand-dot"></span>
      <div class="brand-text">
        <span class="brand-name">MedLift</span>
        <span class="brand-tagline">DISCOUNT PRESCRIPTION DRUG CARD</span>
      </div>
    </div>
    <ul class="member-info">
      <li><span class="member-icon"></span>BIN: 014620</li>
      <li><span class="member-icon"></span>ID: MDL0000</li>
    </ul>
    <div class="rule"></div>
    <div class="code-box">
      <span class="code-label">VELMAR</span>
      <span class="code-number">42917</span>
    </div>
  </section>
</body>
</html>
```